Veltrano - Mechanic/Collision Center Business Card

We're looking for a business card design for our mechanic/ collision repair shop.

Can be with colours or monochromatic.

See the attached files.

Many thanks

```html
<!DOCTYPE html>
<html lang="en">
<head>
<meta charset="utf-8">
<title>Veltrano – Business Card</title>
<link href="https://fonts.googleapis.com/css2?family=Open+Sans:wght@400;600;800&display=swap" rel="stylesheet">
<style>
  :root {
    --page: #e8e8ea;
    --card-white: #ffffff;
    --card-black: #1d1d1e;
    --strip-grey: #3d3d40;
    --strip-black: #1b1b1c;
    --accent-blue: #2196d6;
    --field-grey: #e4e4e6;
    --ink: #2a2a2c;
    --ink-soft: #444448;
    --white: #ffffff;
  }
  * { box-sizing: border-box; margin: 0; padding: 0; }
  html, body {
    width: 1089px; height: 1200px; overflow: hidden;
    background: var(--page);
    font-family: "Open Sans", Arial, sans-serif;
  }
  .canvas { position: relative; width: 1089px; height: 1200px; }
  .card {
    position: absolute; left: 94px; width: 900px; height: 541px;
    box-shadow: 0 12px 30px rgba(0,0,0,.28);
    overflow: hidden;
  }
  .card--front { top: 40px; background: var(--card-white); }
  .card--back { top: 619px; background: var(--card-black); }

  .strip { position: absolute; top: 0; height: 100%; }
  .strip--grey { left: 0; width: 106px; background: var(--strip-grey); }
  .strip--black { left: 106px; width: 77px; background: var(--strip-black); }

  .icon-bar {
    position: absolute; left: 0; width: 183px; height: 61px;
    background: var(--accent-blue);
  }
  .icon-bar svg { position: absolute; left: 128px; top: 14px; width: 33px; height: 33px; }
  .icon-bar--person { top: 141px; }
  .icon-bar--pin { top: 276px; }
  .icon-bar--phone { top: 347px; }
  .icon-bar--screen { top: 418px; }

  .holder { position: absolute; left: 208px; top: 196px; }
  .holder__name { font-size: 29px; color: var(--ink); line-height: 1.1; font-weight: 400; }
  .holder__name strong { font-weight: 800; }
  .holder__role { font-size: 17px; color: var(--accent-blue); margin-top: 2px; }

  .field {
    position: absolute; left: 195px; width: 374px; height: 61px;
    background: var(--field-grey);
    display: flex; flex-direction: column; justify-content: center;
    padding-left: 14px;
    font-size: 15px; color: var(--ink-soft); line-height: 1.35;
  }
  .field--address { top: 276px; }
  .field--phone { top: 347px; }
  .field--web { top: 418px; }

  .brand {
    position: absolute; display: flex; align-items: center; gap: 16px;
    font-weight: 800; letter-spacing: 1px; text-transform: uppercase;
  }
  .brand__dot { border-radius: 50%; background: var(--accent-blue); flex: none; }
  .brand--front { left: 545px; top: 118px; font-size: 46px; color: var(--ink); }
  .brand--front .brand__dot { width: 40px; height: 40px; }
  .brand--back {
    left: 50%; top: 50%; transform: translate(-50%, -50%);
    font-size: 68px; color: var(--white);
  }
  .brand--back .brand__dot { width: 58px; height: 58px; }
</style>
</head>
<body>
<div class="canvas">

  <section class="card card--front" aria-label="Business card front">
    <div class="strip strip--grey"></div>
    <div class="strip strip--black"></div>

    <div class="icon-bar icon-bar--person">
      <svg viewBox="0 0 24 24" fill="#fff"><circle cx="12" cy="8" r="5"/><path d="M3 23c0-5.5 4-9 9-9s9 3.5 9 9z"/></svg>
    </div>
    <div class="icon-bar icon-bar--pin">
      <svg viewBox="0 0 24 24" fill="#fff"><path d="M12 1a8 8 0 0 0-8 8c0 6 8 14 8 14s8-8 8-14a8 8 0 0 0-8-8zm0 11a3 3 0 1 1 0-6 3 3 0 0 1 0 6z"/></svg>
    </div>
    <div class="icon-bar icon-bar--phone">
      <svg viewBox="0 0 24 24" fill="#fff"><path d="M2 8c0-2 3-4 10-4s10 2 10 4v2h-5V8H7v2H2z"/><path d="M6 11h12l3 9H3z"/><circle cx="12" cy="15.5" r="2.5" fill="#2196d6"/></svg>
    </div>
    <div class="icon-bar icon-bar--screen">
      <svg viewBox="0 0 24 24" fill="none" stroke="#fff" stroke-width="2.2"><rect x="2" y="3" width="20" height="14" rx="1"/><path d="M8 21h8M12 17v4"/></svg>
    </div>

    <div class="holder">
      <p class="holder__name"><strong>Rui</strong> Matos</p>
      <p class="holder__role">Manager</p>
    </div>

    <div class="field field--address">Rua das Oficinas, 42 1900-210 Lisboa</div>
    <div class="field field--phone">+351 215550148</div>
    <div class="field field--web">
      <span>veltrano.oficina@mail.pt</span>
      <span>www.veltrano-auto.pt</span>
    </div>

    <div class="brand brand--front">
      <span class="brand__dot"></span>
      <span class="brand__name">Veltrano</span>
    </div>
  </section>

  <section class="card card--back" aria-label="Business card back">
    <div class="brand brand--back">
      <span class="brand__dot"></span>
      <span class="brand__name">Veltrano</span>
    </div>
  </section>

</div>
</body>
</html>
```